Bright Oak Fitness Facility Business Cards

Business Card Design that incorporates the logo and tagline

Target Market(s)

Fitness, People Who Exercise

Contact Information for Business Card

2817 Mossgrove Bend Road
Millbrook, Ohio 44190
Phone: 352-555-Jump (5867)
www.brightoakfitness.example
info@brightoakfitness.example

Requirements
Must have
• Logo, Address, Website, email and tagline "Stronger Daily". Colors should be red/black/grey/white

```html
<!DOCTYPE html>
<html lang="en">
<head>
<meta charset="utf-8">
<title>Bright Oak Fitness – Business Card</title>
<link rel="stylesheet" href="https://fonts.googleapis.com/css2?family=Montserrat:wght@500;600;700&family=Open+Sans:wght@400;600&display=swap">
<style>
  :root {
    --bg: #2a2622;
    --card: #141414;
    --card-hi: #2b2b2b;
    --red: #e3252c;
    --white: #f2f2f2;
    --grey: #b8b8b8;
    --stripe-grey: #cfcfcf;
  }
  * { margin: 0; padding: 0; box-sizing: border-box; }
  html, body { width: 1200px; height: 1023px; overflow: hidden; }
  body {
    background: var(--bg);
    display: flex; align-items: center; justify-content: center;
    font-family: "Open Sans", sans-serif;
  }
  .card {
    position: relative;
    width: 900px; height: 514px;
    border-radius: 22px;
    background: linear-gradient(135deg, var(--card-hi) 0%, var(--card) 55%, #0c0c0c 100%);
    overflow: hidden;
    color: var(--white);
  }
  .brand {
    position: absolute; left: 70px; top: 140px;
    display: flex; align-items: center; gap: 18px;
  }
  .brand-dot { width: 22px; height: 22px; border-radius: 50%; background: var(--red); }
  .brand-name {
    font-family: "Montserrat", sans-serif; font-weight: 700;
    font-size: 40px; letter-spacing: 1px; color: var(--white); line-height: 1.05;
  }
  .brand-sub {
    font-family: "Montserrat", sans-serif; font-weight: 600;
    font-size: 14px; letter-spacing: 7px; color: var(--white); margin-top: 4px;
  }
  .tagline {
    font-family: "Montserrat", sans-serif; font-weight: 500;
    font-size: 14px; letter-spacing: 9px; color: var(--red); margin-top: 10px;
  }
  .person {
    position: absolute; right: 110px; top: 58px; text-align: right;
  }
  .person-name {
    font-family: "Montserrat", sans-serif; font-weight: 600;
    font-size: 36px; letter-spacing: 1px; color: var(--red);
  }
  .person-title { font-size: 20px; color: var(--grey); margin-top: 2px; }
  .stripes {
    position: absolute; right: 0; top: 40px; width: 56px; height: 46px;
    display: flex; flex-direction: column; justify-content: space-between;
  }
  .stripes span { display: block; height: 8px; background: var(--red); }
  .stripes span.light { background: var(--stripe-grey); }
  .divider {
    position: absolute; left: 70px; right: 110px; top: 272px;
    height: 2px; background: var(--red);
  }
  .contacts {
    position: absolute; left: 70px; top: 318px;
    list-style: none; font-size: 21px; line-height: 36px; color: var(--white);
  }
  .contacts li { display: flex; align-items: center; gap: 14px; }
  .contacts svg { width: 14px; height: 14px; fill: var(--red); flex: none; }
  .address {
    position: absolute; right: 110px; top: 300px; text-align: right;
    font-size: 21px; line-height: 34px; color: var(--white);
  }
</style>
</head>
<body>
  <article class="card">
    <div class="brand">
      <span class="brand-dot"></span>
      <div>
        <div class="brand-name">BRIGHT OAK</div>
        <div class="brand-sub">FITNESS</div>
        <div class="tagline">STRONGER DAILY</div>
      </div>
    </div>

    <div class="stripes"><span></span><span class="light"></span><span></span><span></span></div>

    <div class="person">
      <div class="person-name">DANA WHITLOCK</div>
      <div class="person-title">Director</div>
    </div>

    <div class="divider"></div>

    <ul class="contacts">
      <li><svg viewBox="0 0 16 16"><path d="M3 1h3l1.5 4-2 1.3a9 9 0 0 0 4.2 4.2L11 8.5l4 1.5v3a2 2 0 0 1-2 2A13 13 0 0 1 1 3a2 2 0 0 1 2-2z"/></svg>216-555-(5867)</li>
      <li><svg viewBox="0 0 16 16"><path d="M1 3h14v10H1z M2 4l6 5 6-5" fill="none" stroke="#e3252c" stroke-width="1.8"/></svg>info@brightoakfitness.example</li>
      <li><svg viewBox="0 0 16 16"><circle cx="8" cy="8" r="7"/></svg>www.brightoakfitness.example</li>
    </ul>

    <div class="address">
      2817 Mossgrove Bend Road<br>
      Millbrook, Ohio 44190
    </div>
  </article>
</body>
</html>
```